Ledgerwise Reach - B2B Demand Generation Website Project

We need a fully functional website for www.ledgerwisereach.example. We are a B2B Demand Generation company, based in London, working with companies such as QRT, VKD, Norvex, Brindlow, Tarvo generating them sales leads for their sales teams. We run this through digital marketing newsletter promotions and have a network of websites. Content syndication, data, demand generation, online marketing. Our logo has just been redone (attached) and we have a holding page already which i would like to use the style / colours. Our logo is bright and vibrant but i dont want the site to be a rainbow. We are expensive, classy, professorial, B2B, intelligent.

Home
About Us
Our Services
Prospora & QA Technology
Intent Data
Testimonials
Contact Us
Updates

Target Market(s)

B2B Marketers (QRT, Velquarion, Tarvo, VKD, Opal Reach, Driftmoor, Harlow Quantis, Technology Companies, Data Companies, Marketing Teams, Tumbleden.

Industry/Entity Type

Marketing

Coding

Coded - Design and coding required

Number of Pages Required

5+ page

Font styles to use
Sans Serif

Requirements
Must have
• Home
About Us
Our Services
Prospora & QA Technology
Intent Data
Testimonials
Contact Us

Simple Pages.

Look classy, intelligent, data experts. I like the video homepages were the image moves at the top. Very soft animation.
Nice to have
• Websites i like:

https://www.vkd.example/
https://www.brevantor.example/
https://www.plumfieldsites.example.co.uk/

Ledgerwise Reach - The Demand Generation Company
Should not have
• Glimpsevault crap images

```html
<!DOCTYPE html>
<html lang="en">
<head>
<meta charset="utf-8">
<title>Ledgerwise Reach - The Demand Generation Company</title>
<link href="https://fonts.googleapis.com/css2?family=Poppins:ital,wght@0,300;0,400;0,500;0,600;0,700;1,400&display=swap" rel="stylesheet">
<style>
:root{
  --navy:#0b1a2c;
  --navy-deep:#050b14;
  --blue:#1f5aa0;
  --red:#d31f26;
  --ink:#1d1d1f;
  --muted:#555a63;
  --pale:#f4f7fc;
  --line:#e3e7ee;
  --white:#ffffff;
}
*{margin:0;padding:0;box-sizing:border-box}
html,body{width:1200px;height:3062px;overflow:hidden}
body{font-family:"Poppins",sans-serif;color:var(--ink);background:var(--white);position:relative}
.abs{position:absolute}

/* hero */
.hero{left:0;top:0;width:1200px;height:553px;border-bottom-left-radius:150px;overflow:hidden;
  background:radial-gradient(ellipse at 72% 45%,#1d4c78 0%,#0f2c4a 35%,var(--navy) 65%,var(--navy-deep) 100%)}
.brand{left:236px;top:58px;width:164px;text-align:center;color:var(--white)}
.brand-dot{display:block;width:40px;height:40px;border:3px solid var(--white);border-radius:50%;margin:0 auto 6px}
.brand-name{font-size:19px;font-weight:400;letter-spacing:.2px;line-height:1}
.brand-tag{font-size:7px;margin-top:3px;opacity:.85}
.topline{top:30px;color:var(--white);display:flex;align-items:center;gap:8px}
.topline small{display:block;font-size:6.5px;font-weight:500}
.topline b{display:block;font-size:10.5px;font-weight:400;color:var(--red)}
.nav{left:441px;top:80px;display:flex;gap:17px;font-size:8.6px;font-weight:600;color:var(--white)}
.nav a{color:inherit;text-decoration:none}
.nav .current{color:var(--red);border-bottom:1px solid var(--red);padding-bottom:6px}
.play{left:547px;top:245px}
.hero-title{left:0;top:358px;width:1210px;text-align:center;font-size:32px;font-weight:600;color:var(--white)}

/* welcome */
.divider{left:608px;top:553px;width:1px;height:84px;background:#cfd5de}
.welcome-photo{left:278px;top:612px;width:290px;height:290px;border-radius:50%;
  background:radial-gradient(circle,#c9d5e2 0%,#9fb3c8 40%,var(--blue) 42%,#e04148 44%,#f6d2d3 100%)}
.eyebrow{left:610px;top:665px;font-size:11.5px;font-weight:600}
.welcome-name{left:609px;top:677px;font-size:33px;font-weight:400;color:var(--red)}
.welcome-text{left:610px;top:727px;width:310px;font-size:10.2px;line-height:16.3px;color:var(--ink)}

/* partners */
.partners{left:0;top:965px;width:1200px;height:285px;background:var(--pale)}
.partners h2{position:absolute;left:0;top:52px;width:1200px;text-align:center;font-size:23px;font-weight:400}
.partners p{position:absolute;left:0;top:93px;width:1200px;text-align:center;font-size:10px}
.stat{top:148px;width:220px;text-align:center}
.stat small{display:block;font-size:11px;color:var(--blue)}
.stat strong{display:block;font-size:39px;font-weight:300;line-height:1.1}
.stat span{display:block;font-size:11px;font-weight:600;margin-top:3px}

/* services */
.blob{left:-80px;top:1330px;width:760px;height:440px;border-radius:50%;background:#f6f8fc;transform:rotate(-8deg)}
.section-title{left:0;width:1200px;text-align:center;font-size:33px;font-weight:400}
.section-title .r{color:var(--red)}
.section-title .b{color:var(--blue)}
.card{top:1383px;width:230px;height:270px;background:var(--white);box-shadow:0 2px 10px rgba(20,40,80,.06);text-align:center;padding:22px 22px 0}
.card svg{display:block;margin:0 auto}
.card h3{font-size:12px;font-weight:600;line-height:18px;margin-top:14px}
.card p{font-size:11px;line-height:18.6px;margin-top:12px;color:var(--ink)}
.card .more{position:absolute;left:0;bottom:28px;width:230px;text-align:center;color:#c5c9d0;font-size:14px}

/* testimonials */
.avatar{border-radius:50%;background:linear-gradient(150deg,#d9b9a4,#8b5a44)}
.avatar.faded{opacity:.18}
.person{width:200px;text-align:center}
.person b{display:block;font-size:12px;font-weight:400;color:#3a3a3a}
.person small{display:block;font-size:8px;color:#3a3a3a;margin-top:2px}
.person.faded{opacity:.15}
.quote{font-size:14.5px;font-style:italic;line-height:21px;white-space:nowrap}
.quote.faded{opacity:.12}
.dots{left:571px;top:2104px;display:flex;gap:14px}
.dots i{width:5px;height:5px;border-radius:50%;background:#e9b1b4}
.dots i:first-child{background:var(--red)}

/* contact */
.contact{left:0;top:2222px;width:1200px;height:476px;background:var(--pale)}
.contact h2{position:absolute;left:235px;top:68px;font-size:22.5px;font-weight:600;line-height:30px}
.contact p{position:absolute;left:235px;top:136px;width:400px;font-size:10.2px;line-height:15px}
.tab{left:235px;top:2417px;width:30px;height:163px;background:var(--blue);color:var(--white)}
.tab span{position:absolute;left:15px;top:81px;transform:translate(-50%,-50%) rotate(-90deg);font-size:9.5px;font-weight:600;letter-spacing:2px;white-space:nowrap}
.field{background:var(--white);font-size:9.5px;color:#777;padding:9px 15px}
.submit{left:551px;top:2598px;width:111px;height:31px;border-radius:16px;background:var(--red);color:var(--white);font-size:10.5px;font-weight:600;text-align:center;line-height:31px}
.desk-photo{left:712px;top:2270px;width:488px;height:428px;background:linear-gradient(135deg,#e9edf2 0%,#cfd6de 45%,#20324b 70%,#e8e2dc 100%)}

/* footer */
.foot-brand{left:236px;top:2750px;width:250px;text-align:center}
.foot-brand .brand-dot{border-color:var(--red)}
.foot-brand .brand-name{color:var(--red);font-size:22px}
.foot-brand .brand-tag{color:var(--blue);opacity:1}
.foot-about{left:236px;top:2856px;width:250px;text-align:center;font-size:9.2px;line-height:15px}
.col h4{font-size:10.5px;font-weight:600;letter-spacing:.5px;margin-bottom:12px}
.col li{list-style:none;font-size:9.2px;line-height:17.6px}
.contact-line{display:flex;gap:8px;font-size:9.2px;line-height:15px;margin-bottom:10px}
.contact-line svg{flex:none;margin-top:2px}
.copy{left:236px;top:2992px;font-size:9px}
.social{top:2985px;width:24px;height:24px;border-radius:50%;background:#c9c9c9}
</style>
</head>
<body>

<section class="abs hero" role="img" aria-label="Dark blue abstract background of flowing dotted data waves"></section>

<div class="abs brand">
  <span class="brand-dot"></span>
  <div class="brand-name">Ledgerwise Reach</div>
  <div class="brand-tag">The Demand Generation Company</div>
</div>

<div class="abs topline" style="left:672px">
  <svg width="20" height="16" viewBox="0 0 20 16"><rect x="1" y="3" width="18" height="12" fill="none" stroke="#fff" stroke-width="1.3"/><path d="M1 3 L10 10 L19 3" fill="none" stroke="#fff" stroke-width="1.3"/></svg>
  <div><small>EMAIL US NOW:</small><b>info@ledgerwisereach.example</b></div>
</div>
<div class="abs topline" style="left:848px">
  <svg width="18" height="18" viewBox="0 0 18 18"><path d="M4 2 L7 5 L5 8 Q7 12 10 13 L13 11 L16 14 L13 17 Q4 15 1 5 Z" fill="none" stroke="#fff" stroke-width="1.2"/></svg>
  <div><small>CALL US NOW:</small><b>(020) 555-0148</b></div>
</div>

<nav class="abs nav">
  <a class="current">HOME</a><a>ABOUT US</a><a>OUR SERVICES</a><a>PROSPORA &amp; QA TECHNOLOGY</a><a>INTENT DATA</a><a>TESTIMONIALS</a><a>CONTACT US</a>
</nav>

<svg class="abs play" width="90" height="90" viewBox="0 0 90 90" aria-label="Play video">
  <circle cx="45" cy="45" r="38" fill="none" stroke="#fff" stroke-width="2" stroke-dasharray="2 4"/>
  <circle cx="45" cy="45" r="24" fill="none" stroke="#fff" stroke-width="5"/>
  <path d="M40 35 L55 45 L40 55 Z" fill="#fff"/>
</svg>
<h1 class="abs hero-title">The Demand&nbsp; Generation Company</h1>

<div class="abs divider"></div>
<div class="abs welcome-photo" role="img" aria-label="Photo of two colleagues working at a desk, framed in a speech-bubble ring"></div>
<div class="abs eyebrow">WELCOME TO</div>
<div class="abs welcome-name">Ledgerwise Reach</div>
<p class="abs welcome-text">Ledgerwise Reach offers multi-channel demand generation services to publishers and technology vendors through our network of lead generation websites and native speaking telemarketing agents. Whether looking for MQL, ABM or BANT campaigns, Ledgerwise Reach can assist you in delivering your demand generation strategy and generate pipeline for your sales teams and/or channel partners.</p>

<section class="abs partners">
  <h2>WHO WE WORK WITH</h2>
  <p>QRT, Tarvo, VKD, Korrin, Cloudmere, Stavelane, Tallyworth, Quennex, Brightfold</p>
  <div class="abs stat" style="left:279px"><small>Ticker to</small><strong>70,000+</strong><span>Downloads Per Month</span></div>
  <div class="abs stat" style="left:487px"><small>Ticker to</small><strong>25,000+</strong><span>Leads Delivered Per Month</span></div>
  <div class="abs stat" style="left:699px"><small>Ticker to</small><strong>50+</strong><span>Countries We Can Reach</span></div>
</section>

<div class="abs blob"></div>
<h2 class="abs section-title" style="top:1298px"><span class="r">our</span> <span class="b">services</span></h2>

<article class="abs card" style="left:236px">
  <svg width="62" height="50" viewBox="0 0 62 50" fill="none" stroke="#1f5aa0" stroke-width="2"><circle cx="31" cy="18" r="6"/><path d="M20 36 Q31 22 42 36"/><circle cx="14" cy="28" r="4"/><circle cx="48" cy="28" r="4"/><path d="M4 44 Q14 32 24 44 M38 44 Q48 32 58 44 M4 44 H58"/><path d="M31 2 V6 M20 7 L23 10 M42 7 L39 10"/></svg>
  <h3>MARKETING QUALIFIED LEADS (MQL)</h3>
  <p>A Marketing Qualified Lead (MQL) is a prospect that has expressed an interest in what your brand has to offer.</p>
  <div class="more">⟶</div>
</article>
<article class="abs card" style="left:486px">
  <svg width="62" height="58" viewBox="0 0 62 58" fill="none" stroke="#1f5aa0" stroke-width="2"><rect x="8" y="4" width="38" height="50" rx="2"/><rect x="24" y="20" width="30" height="34" rx="2"/><circle cx="16" cy="38" r="5"/><path d="M14 16 V24 M19 12 V24 M24 14 V24"/><path d="M29 26 H49 M29 34 H33 M37 34 H41 M45 34 H49 M29 41 H33 M37 41 H41 M45 41 H49 M29 48 H33 M37 48 H41 M45 48 H49"/></svg>
  <h3>ACCOUNT BASED MARKETING LEADS (ABM)</h3>
  <p>ABM is a strategy that directs marketing resources to engaging a specific set of target accounts.</p>
  <div class="more">⟶</div>
</article>
<article class="abs card" style="left:734px">
  <svg width="62" height="52" viewBox="0 0 62 52" fill="none" stroke="#1f5aa0" stroke-width="2"><circle cx="12" cy="12" r="7"/><path d="M6 48 V36 M13 48 V30 M20 48 V32 M27 48 V26 M34 48 V28 M41 48 V20 M48 48 V16 M55 48 V8"/><path d="M8 32 L26 20 L34 24 L54 6 M46 6 H54 V14"/></svg>
  <h3>SALES QUALIFIED LEAD<br>/ BANT</h3>
  <p>An SQL lead or a BANT lead is a type of lead that expressed a specific interest in a product and service that you have to offer...</p>
  <div class="more">⟶</div>
</article>

<h2 class="abs section-title" style="top:1808px"><span class="b">testimonials</span></h2>

<div class="abs avatar faded" role="img" aria-label="Client portrait" style="left:182px;top:1892px;width:60px;height:60px"></div>
<div class="abs person faded" style="left:112px;top:1968px"><b>DELIA MARSH</b><small>SALES MANAGER</small></div>
<div class="abs avatar faded" role="img" aria-label="Client portrait" style="left:968px;top:1892px;width:60px;height:60px"></div>
<div class="abs person faded" style="left:898px;top:1968px"><b>DELIA MARSH</b><small>SALES MANAGER</small></div>

<svg class="abs" style="left:332px;top:1926px" width="22" height="16" viewBox="0 0 22 16" fill="none" stroke="#222" stroke-width="2"><path d="M21 8 H2 M9 1 L2 8 L9 15"/></svg>
<svg class="abs" style="left:846px;top:1926px" width="22" height="16" viewBox="0 0 22 16" fill="none" stroke="#222" stroke-width="2"><path d="M1 8 H20 M13 1 L20 8 L13 15"/></svg>

<div class="abs avatar" role="img" aria-label="Portrait of the client giving the testimonial" style="left:566px;top:1888px;width:68px;height:68px"></div>
<div class="abs person" style="left:500px;top:1968px"><b>DELIA MARSH</b><small>SALES MANAGER</small></div>

<div class="abs quote faded" style="left:20px;top:2019px">Lorem ipsum dolor sit amet, consectetur adipiscing elit.</div>
<div class="abs quote faded" style="left:6px;top:2040px">Nunc sit amet libero tristique, semper est vitae, mattis felis.</div>
<div class="abs quote" style="left:407px;top:2019px">Lorem ipsum dolor sit amet, consectetur adipiscing elit.</div>
<div class="abs quote" style="left:394px;top:2040px">Nunc sit amet libero tristique, semper est vitae, mattis felis.</div>
<div class="abs quote faded" style="left:806px;top:2019px">Lorem ipsum dolor sit amet, consectetur adipiscing elit.</div>
<div class="abs quote faded" style="left:790px;top:2040px">Nunc sit amet libero tristique, semper est vitae, mattis felis.</div>
<div class="abs dots"><i></i><i></i><i></i><i></i></div>

<section class="abs contact">
  <h2>Contact us today,<br>We are here to help you</h2>
  <p>Lorem ipsum dolor sit amet, consectetur adipiscing elit. Duis libero sapien, sodales a scelerisque eget, aliquet at arcu.</p>
</section>
<div class="abs tab"><span>GET IN TOUCH</span></div>
<div class="abs field" style="left:278px;top:2417px;width:187px;height:30px">First name</div>
<div class="abs field" style="left:476px;top:2417px;width:187px;height:30px">Last name</div>
<div class="abs field" style="left:278px;top:2460px;width:187px;height:30px">Email address</div>
<div class="abs field" style="left:476px;top:2460px;width:187px;height:30px">Phone</div>
<div class="abs field" style="left:278px;top:2505px;width:385px;height:74px">Your comments</div>
<div class="abs submit">Submit Now</div>
<div class="abs desk-photo" role="img" aria-label="Photo of hands typing on a laptop beside a coffee cup, a plant and a pen"></div>

<div class="abs foot-brand">
  <span class="brand-dot"></span>
  <div class="brand-name">Ledgerwise Reach</div>
  <div class="brand-tag">The Demand Generation Company</div>
</div>
<p class="abs foot-about">Ledgerwise Reach can deliver high quality sales leads from any country in the world. This can include leads via email or telemarketing, account-based targeting (ABM) or identifying need and pain points through BANT / SQL campaigns.</p>

<div class="abs col" style="left:532px;top:2766px">
  <h4>PAGES</h4>
  <ul><li>Home</li><li>About Us</li><li>Our Services</li><li>Prospora &amp; QA</li><li>Technology</li><li>Intent Data</li><li>Testimonials</li><li>Contact Us</li></ul>
</div>
<div class="abs col" style="left:643px;top:2766px">
  <h4>RESORCE</h4>
  <ul><li>FAQ</li><li>Terms &amp; Conditions</li><li>Privacy Policy</li><li>Sitemap</li></ul>
</div>
<div class="abs col" style="left:768px;top:2766px">
  <h4>CONTACT</h4>
  <div class="contact-line"><svg width="10" height="13" viewBox="0 0 10 13"><path d="M5 0 A5 5 0 0 1 10 5 C10 8 5 13 5 13 C5 13 0 8 0 5 A5 5 0 0 1 5 0Z" fill="#1f5aa0"/><circle cx="5" cy="5" r="2" fill="#fff"/></svg><span>Harrow Lane<br>42 London, England<br>EC2 9ZZ, GB</span></div>
  <div class="contact-line"><svg width="10" height="10" viewBox="0 0 18 18"><path d="M4 2 L7 5 L5 8 Q7 12 10 13 L13 11 L16 14 L13 17 Q4 15 1 5 Z" fill="#1f5aa0"/></svg><span>(020) 555-0148</span></div>
  <div class="contact-line"><svg width="11" height="9" viewBox="0 0 20 16"><rect x="1" y="2" width="18" height="13" fill="#1f5aa0"/><path d="M1 2 L10 9 L19 2" fill="none" stroke="#fff" stroke-width="1.5"/></svg><span>info@ledgerwisereach.example</span></div>
</div>

<div class="abs copy">© 2020 Ledgerwise Reach. All Rights Reserved.</div>
<div class="abs social" style="left:865px" aria-label="Social profile"></div>
<div class="abs social" style="left:898px" aria-label="Social profile"></div>

</body>
</html>
```